Keynote slides for football/soccer companies videos

I am looking for an array of slides to be used within my videos.
These templates should all be for Apple Keynote

Please see my Instagram feed to see the kind of look that I am looking for to keep me onbrand

https://instagram.com/officialdavidrennick

You can also see my website at https://pitchlane.example

Target Market(s)

Footballers

Requirements
Must have
• Be onbrand in the look of the images of my Instagram feed

```html
<!DOCTYPE html>
<html lang="en">
<head>
<meta charset="utf-8">
<title>Pitchlane Keynote Slides</title>
<link href="https://fonts.googleapis.com/css2?family=Montserrat:wght@400;500;600;700;800;900&display=swap" rel="stylesheet">
<style>
:root{
  --navy:#0b2131;
  --navy-deep:#061521;
  --blue:#1591d8;
  --blue-mid:#0f6fa8;
  --cyan:#14b2ec;
  --pink:#e8246b;
  --white:#ffffff;
  --ink:#3a4a5a;
  --muted:#b8c7d4;
}
*{margin:0;padding:0;box-sizing:border-box}
html,body{width:1200px;height:687px;overflow:hidden;background:var(--white)}
body{position:relative;font-family:'Montserrat',sans-serif;color:var(--white)}
.slide{position:absolute;width:391px;height:221px;overflow:hidden;background:var(--navy)}
.slide--title{left:0;top:110px}
.slide--reasons-intro{left:404px;top:0}
.slide--reviews-cover{left:808px;top:0;width:392px}
.slide--who{left:0;top:344px}
.slide--reasons-list{left:404px;top:233px;background:var(--white);border:1px solid #e6e9ee}
.slide--review{left:808px;top:233px;width:392px}
.slide--videos{left:404px;top:466px}
.slide--thanks{left:808px;top:466px;width:392px}
.field-photo{position:absolute;inset:0;background:radial-gradient(ellipse at 40% 70%,#1d4a66 0%,#12344c 45%,#081a28 100%)}
.shapes{position:absolute;inset:0;width:100%;height:100%}
.brand{position:absolute;display:flex;align-items:center;gap:4px;font-weight:800;letter-spacing:.2px}
.brand__dot{border:1.5px solid var(--white);border-radius:50%}
.brand--large{left:15px;top:17px;font-size:14px}
.brand--large .brand__dot{width:17px;height:17px}
.brand__tag{display:block;font-size:3.6px;font-weight:600;letter-spacing:.3px;margin-top:1px}
.brand--small{right:8px;bottom:8px;font-size:5.5px}
.brand--small .brand__dot{width:8px;height:8px;border-width:1px}
.hl{display:inline-block;padding:0 3px;font-weight:800;line-height:1.15}
.hl--pink{background:var(--pink);color:var(--white)}
.hl--cyan{background:var(--cyan);color:var(--white)}
.byline{position:absolute;text-align:right}
.byline__name{font-size:7.5px;font-weight:500}
.byline__role{font-size:4.6px;margin-top:3px}
.title-main{position:absolute;left:17px;top:72px;font-size:26.5px;font-weight:900;line-height:25px;letter-spacing:.3px}
.goal-photo{position:absolute;left:55px;top:118px;width:280px;height:100px;background:linear-gradient(180deg,#1f4d86 0%,#1a3f78 50%,#0b1c3d 100%);opacity:.85}
.reasons-heading{position:absolute;left:17px;top:20px}
.reasons-heading__num{font-size:29px;font-weight:800;color:var(--pink);line-height:1}
.reasons-heading__line{font-size:14px;font-weight:800;line-height:1.1}
.reasons-heading .hl{font-size:14px;margin-top:3px}
.reviews-band{position:absolute;left:0;top:0;width:93px;height:221px;background:#000}
.boots-photo{position:absolute;left:93px;top:0;right:0;bottom:0;background:linear-gradient(120deg,#2b3a3c 0%,#3a4a4c 45%,#8f9a9b 55%,#2f3d3f 70%,#c9562c 90%)}
.reviews-title{position:absolute;left:9px;top:65px;display:flex;flex-direction:column;align-items:flex-start;gap:1px}
.reviews-title .hl--sm{font-size:14px}
.reviews-title .hl--lg{font-size:29px;line-height:1.05}
.who-heading{position:absolute;left:17px;top:24px}
.who-heading__pre{font-size:8px;font-weight:700;margin-bottom:3px}
.who-heading .hl{font-size:14px}
.book{position:absolute;left:18px;top:69px;width:60px;height:62px;background:linear-gradient(135deg,#2a2f38,#0f1218)}
.copy{font-size:4.2px;line-height:1.35;color:var(--muted)}
.copy strong{color:var(--white);font-weight:700}
.who-bio{position:absolute;left:89px;top:76px;width:85px}
.who-bio p+p{margin-top:4px}
.who-more{position:absolute;left:17px;top:146px;width:165px}
.who-more p+p{margin-top:4px}
.portrait{position:absolute;left:225px;top:0;width:160px;height:221px;background:linear-gradient(180deg,#8e6a5a 0%,#2d3d5a 55%,#1c2a44 100%)}
.rl-heading{position:absolute;left:17px;top:16px;display:flex;flex-direction:column;align-items:flex-start;gap:2px}
.rl-heading .hl--sm{font-size:12px}
.rl-heading .hl--lg{font-size:21px}
.rl-heading small{font-size:11px}
.rl-item{position:absolute;left:17px;display:flex;gap:12px;align-items:flex-start;width:160px}
.rl-item__icon{width:14px;height:14px;flex:none;margin-top:3px}
.rl-item .copy{color:#6f86a8;font-size:4.2px}
.stadium{position:absolute;inset:0;width:100%;height:100%}
.review-heading{position:absolute;left:13px;top:12px}
.review-heading__pre{font-size:5.5px;font-weight:700;margin-bottom:2px}
.review-heading .hl{font-size:11px}
.quote-mark{position:absolute;left:15px;top:44px;font-size:22px;font-weight:800;line-height:1}
.review-quote{position:absolute;left:33px;top:60px;width:130px}
.review-quote p+p{margin-top:4px}
.stat-head{position:absolute;left:18px;top:143px;display:flex;align-items:center;gap:3px;width:210px}
.stat-head__icon{width:13px;height:9px}
.stat-head .hl{font-size:5px;padding:1px 2px}
.stat-head__rule{flex:1;height:.6px;background:var(--muted);margin-left:4px}
.stat-col{position:absolute;top:160px}
.stat-col h4{font-size:5px;font-weight:700;margin-bottom:4px}
.stat-col--a{left:17px;width:95px}
.stat-col--b{left:122px;width:120px}
.stat-goals{font-size:5px;font-weight:700;margin-top:8px}
.stat-goals span{font-weight:400;font-size:4px}
.player{position:absolute;left:262px;top:0;width:120px;height:221px;background:linear-gradient(180deg,#5a4038 0%,#c9333a 40%,#e8e4e4 60%,#c9333a 100%)}
.club-badge{position:absolute;left:351px;top:24px;width:24px;height:28px;background:var(--white);border-radius:2px}
.club-name{position:absolute;left:340px;top:56px;width:48px;text-align:center;font-size:5px;line-height:1.3}
.videos-heading{position:absolute;left:10px;top:9px;display:flex;flex-direction:column;align-items:flex-start;gap:2px}
.videos-heading .hl{font-size:17px}
.video-frame{position:absolute;left:90px;top:26px;width:301px;height:167px;background:#000;display:flex;align-items:center;justify-content:center}
.video-frame svg{width:40px;height:40px}
.thanks-title{position:absolute;left:14px;top:96px;font-size:30px;font-weight:900}
.thanks-brand{left:14px;top:79px;font-size:9px}
.thanks-brand .brand__dot{width:14px;height:14px}
.thanks-by{position:absolute;left:16px;top:177px}
.thanks-by .byline__name{font-size:7.5px}
.thanks-url{position:absolute;left:16px;top:204px;font-size:4.8px}
</style>
</head>
<body>

<section class="slide slide--title">
  <div class="field-photo" role="img" aria-label="Close-up photograph of pitch grass in blue tones"></div>
  <svg class="shapes" viewBox="0 0 391 221" aria-hidden="true">
    <polygon points="240,0 330,0 391,60 391,221 300,221 180,110" fill="var(--blue-mid)" opacity=".55"/>
    <polygon points="230,40 330,140 300,170 200,70" fill="var(--blue)" opacity=".5"/>
    <polygon points="330,0 391,0 391,40 360,10" fill="var(--blue)"/>
    <polygon points="360,160 391,130 391,190" fill="var(--blue)"/>
  </svg>
  <div class="brand brand--large"><span class="brand__dot"></span><span>PITCHLANE<span class="brand__tag">TRAIN THE MIND, LIFT THE GAME</span></span></div>
  <h1 class="title-main">TITTLE<br>GOES<br>HERE</h1>
  <div class="byline" style="right:13px;top:194px"><div class="byline__name">by David Rennick</div><div class="byline__role">Football Mindset Trainer</div></div>
</section>

<section class="slide slide--reasons-intro">
  <div class="field-photo" style="background:linear-gradient(135deg,#061228 0%,#0b1f3d 60%,#06142a 100%)"></div>
  <div class="goal-photo" role="img" aria-label="Photograph of a goalkeeper diving in front of a goal net"></div>
  <svg class="shapes" viewBox="0 0 391 221" aria-hidden="true">
    <polygon points="260,0 391,0 391,90 330,150 240,60" fill="var(--blue)" opacity=".55"/>
    <polygon points="300,120 391,40 391,210" fill="var(--blue)" opacity=".45"/>
  </svg>
  <div class="reasons-heading">
    <div class="reasons-heading__num">3 Reasons</div>
    <div class="reasons-heading__line">why Footballers<br>don't use</div>
    <span class="hl hl--cyan">Sports Psychologists</span>
  </div>
  <div class="brand brand--small"><span class="brand__dot"></span>PITCHLANE</div>
</section>

<section class="slide slide--reviews-cover">
  <div class="boots-photo" role="img" aria-label="Photograph of orange football boots on artificial turf beside a white line"></div>
  <div class="reviews-band"></div>
  <div class="reviews-title">
    <span class="hl hl--cyan hl--sm">Reviews of</span>
    <span class="hl hl--pink hl--lg">David's</span>
    <span class="hl hl--cyan hl--lg">work</span>
  </div>
  <div class="brand brand--small" style="top:9px;bottom:auto"><span class="brand__dot"></span>PITCHLANE</div>
</section>

<section class="slide slide--who">
  <div class="field-photo" role="img" aria-label="Close-up photograph of pitch grass in blue tones"></div>
  <svg class="shapes" viewBox="0 0 391 221" aria-hidden="true">
    <polygon points="250,0 330,0 391,60 391,180 300,90" fill="var(--blue)"/>
    <polygon points="205,10 225,0 235,10 215,22" fill="var(--blue)"/>
    <polygon points="340,200 391,150 391,221 330,221" fill="var(--blue)" opacity=".7"/>
  </svg>
  <div class="portrait" role="img" aria-label="Portrait photograph of the trainer in a blue checked blazer"></div>
  <div class="who-heading"><div class="who-heading__pre">Who is</div><span class="hl hl--pink">David Rennick?</span></div>
  <div class="book" role="img" aria-label="Book cover of Think Sharp, Play Sharp"></div>
  <div class="who-bio copy">
    <p>David Rennick is one of the most trusted Mental Performance experts in the modern game.</p>
    <p>He is the best selling author of the 'football bible' <strong>Think Sharp, Play Sharp</strong> The Professional Footballers Guide to Peak Performance</p>
  </div>
  <div class="who-more copy">
    <p>He continues to take the most cutting edge approaches from psychology, neuroscience and other areas and provide them to players in an easy to use and inspiring way that gets results.</p>
    <p>Just like the modern day football player, he is used to working in highly pressurised environments where there is a requirement to perform to a very high level.</p>
  </div>
  <div class="brand brand--small"><span class="brand__dot"></span>PITCHLANE</div>
</section>

<section class="slide slide--reasons-list">
  <svg class="stadium" viewBox="0 0 391 221" role="img" aria-label="Photograph of a floodlit football stadium pitch">
    <defs>
      <linearGradient id="stadiumTone" x1="0" y1="0" x2="0" y2="1">
        <stop offset="0" stop-color="#0d2a44"/><stop offset=".45" stop-color="#1b5d72"/><stop offset="1" stop-color="#2f8a3e"/>
      </linearGradient>
    </defs>
    <polygon points="391,0 391,221 255,221" fill="var(--blue)" opacity=".5"/>
    <polygon points="391,40 391,221 275,221 225,170 370,30" fill="url(#stadiumTone)"/>
    <polygon points="330,0 391,0 391,40 360,30" fill="var(--blue-mid)"/>
  </svg>
  <div class="rl-heading">
    <span class="hl hl--pink hl--sm">The</span>
    <span class="hl hl--pink hl--lg">Reasons <small>are..</small></span>
  </div>
  <div class="rl-item" style="top:78px"><svg class="rl-item__icon" viewBox="0 0 14 14" aria-hidden="true"><circle cx="7" cy="7" r="6" fill="none" stroke="var(--blue)" stroke-width=".9"/><polygon points="7,4.5 9.3,6.2 8.4,9 5.6,9 4.7,6.2" fill="none" stroke="var(--blue)" stroke-width=".7"/></svg><p class="copy">Lorem Ipsum is simply dummy text of the printing and typesetting industry. Lorem Ipsum has been the industry's standard dummy text ever since the 1500s, when an unknown printer took a galley of type and scrambled it to make a type specimen book</p></div>
  <div class="rl-item" style="top:119px"><svg class="rl-item__icon" viewBox="0 0 14 14" aria-hidden="true"><circle cx="7" cy="7" r="6" fill="none" stroke="var(--blue)" stroke-width=".9"/><polygon points="7,4.5 9.3,6.2 8.4,9 5.6,9 4.7,6.2" fill="none" stroke="var(--blue)" stroke-width=".7"/></svg><p class="copy">Lorem Ipsum is simply dummy text of the printing and typesetting industry. Lorem Ipsum has been the industry's standard dummy text ever since the 1500s, when an unknown printer took a galley of type and scrambled it to make a type specimen book</p></div>
  <div class="rl-item" style="top:160px"><svg class="rl-item__icon" viewBox="0 0 14 14" aria-hidden="true"><circle cx="7" cy="7" r="6" fill="none" stroke="var(--blue)" stroke-width=".9"/><polygon points="7,4.5 9.3,6.2 8.4,9 5.6,9 4.7,6.2" fill="none" stroke="var(--blue)" stroke-width=".7"/></svg><p class="copy">Lorem Ipsum is simply dummy text of the printing and typesetting industry. Lorem Ipsum has been the industry's standard dummy text ever since the 1500s, when an unknown printer took a galley of type and scrambled it to make a type specimen book</p></div>
  <div class="brand brand--small"><span class="brand__dot"></span>PITCHLANE</div>
</section>

<section class="slide slide--review">
  <div class="field-photo" role="img" aria-label="Close-up photograph of pitch grass in blue tones"></div>
  <svg class="shapes" viewBox="0 0 392 221" aria-hidden="true">
    <polygon points="230,0 392,0 392,120 300,200 220,120 280,60" fill="var(--blue)"/>
    <polygon points="225,10 240,0 250,10 235,22" fill="var(--blue)"/>
    <polygon points="360,221 392,190 392,221" fill="var(--blue)"/>
  </svg>
  <div class="player" role="img" aria-label="Photograph of a footballer in a red and white striped kit"></div>
  <div class="club-badge" aria-hidden="true"></div>
  <div class="club-name">Callum Hendry<br>Harbour City</div>
  <div class="review-heading"><div class="review-heading__pre">Review of</div><span class="hl hl--pink">David's Works</span></div>
  <div class="quote-mark" aria-hidden="true">”</div>
  <div class="review-quote copy">
    <p>Having now spent well over 24 hours focussed 1 to 1 work with David over the course of a Footballing season, I can say his input has helped to improve my performances.</p>
    <p>On a daily basis with my motivation, focus and intensity in training. On match days with my confidence and preparing my mind as well as my body.</p>
    <p>And my recovery, shutting down from night games, improving my sleep and positive mentality. I look forward to working with David well into the future and believe working the mind is crucial and a great area for many pro's in the game.</p>
  </div>
  <div class="stat-head">
    <svg class="stat-head__icon" viewBox="0 0 13 9" aria-hidden="true"><rect x="0" y="6" width="2" height="3" fill="#fff"/><rect x="3.5" y="4" width="2" height="5" fill="#fff"/><rect x="7" y="5" width="2" height="4" fill="#fff"/><rect x="10.5" y="2" width="2" height="7" fill="#fff"/><polyline points="1,4 4.5,2 8,3 11.5,0.5" fill="none" stroke="#fff" stroke-width=".6"/></svg>
    <span class="hl hl--cyan">Statistic</span><span class="stat-head__rule"></span>
  </div>
  <div class="stat-col stat-col--a copy">
    <h4>Duals</h4>
    <p>Duals Duals Won: 2% Improvement<br>Defensive Duals Won: 1.8% Improvement<br>Offensive Duals Won: 98% Improvement<br>Successful Sliding Tackles: 12% improvement</p>
    <p class="stat-goals">Goals: 2 <span>(last season 0)</span></p>
  </div>
  <div class="stat-col stat-col--b copy" style="top:158px">
    <h4>In Possession</h4>
    <p>In Possession Losses (own half): 4.2% improvement<br>Passing Accuracy: 4% Improvement<br>Long Pass Accuracy: 7.5% Improvement<br>Passes to Final Third Accuracy: 16% Improvement<br>Passes to Box Accuracy: 49.7% Improvement<br>Accurate Forward Passes: 7% Improvement<br>Successful Dribbles: 44% Improvement</p>
  </div>
  <div class="brand brand--small"><span class="brand__dot"></span>PITCHLANE</div>
</section>

<section class="slide slide--videos">
  <div class="field-photo" role="img" aria-label="Close-up photograph of pitch grass in blue tones"></div>
  <svg class="shapes" viewBox="0 0 391 221" aria-hidden="true">
    <polygon points="220,0 300,0 250,26 220,26" fill="var(--blue)"/>
    <polygon points="330,0 391,0 391,26 300,26" fill="var(--blue)" opacity=".8"/>
    <polygon points="260,193 320,193 290,221 240,221" fill="var(--blue)"/>
  </svg>
  <div class="videos-heading"><span class="hl hl--cyan">Our</span><span class="hl hl--pink">Videos</span></div>
  <div class="video-frame"><svg viewBox="0 0 40 40" aria-label="Play"><circle cx="20" cy="20" r="18" fill="none" stroke="#fff" stroke-width="2"/><polygon points="16,12 28,20 16,28" fill="none" stroke="#fff" stroke-width="2" stroke-linejoin="round"/></svg></div>
  <div class="brand brand--small"><span class="brand__dot"></span>PITCHLANE</div>
</section>

<section class="slide slide--thanks">
  <div class="field-photo" role="img" aria-label="Close-up photograph of pitch grass in blue tones"></div>
  <svg class="shapes" viewBox="0 0 392 221" aria-hidden="true">
    <polygon points="230,0 320,0 392,70 392,210 330,160 250,80 300,30" fill="var(--blue)" opacity=".6"/>
    <polygon points="340,0 392,0 392,30" fill="var(--blue)"/>
    <polygon points="345,190 392,145 392,200 365,221" fill="var(--blue)"/>
  </svg>
  <div class="brand brand--large thanks-brand"><span class="brand__dot"></span><span>PITCHLANE<span class="brand__tag">TRAIN THE MIND, LIFT THE GAME</span></span></div>
  <h2 class="thanks-title">Thank You</h2>
  <div class="thanks-by" style="text-align:left"><div class="byline__name">by David Rennick</div><div class="byline__role">Football Mindset Trainer</div></div>
  <div class="thanks-url">https://pitchlane.example</div>
</section>

</body>
</html>
```